BASIC website restyle: graphic + coding

I need a restyle of our present website. Same contents, but better graphic.
It will be temporary until we'll have defined the strategy and so we'll have the definitive one.
I would need a fast job including coding.

I uploaded some picture that you're free to use.
I also extended of 1 day, no more extensions will be possible.

```html
<!DOCTYPE html>
<html lang="en">
<head>
<meta charset="utf-8">
<title>Silvane SA</title>
<link rel="stylesheet" href="https://fonts.googleapis.com/css2?family=Roboto:wght@300;400;700&display=swap">
<style>
  :root {
    --green: #0a8744;
    --slate: #3b4e63;
    --slate-dark: #2f3f51;
    --text: #333c47;
    --muted: #8ea8c4;
    --rule: #d6d9dd;
    --sky-light: #a4b5c8;
    --sky-dark: #8599b0;
  }
  * { box-sizing: border-box; margin: 0; padding: 0; }
  html, body { width: 1200px; height: 1100px; overflow: hidden; }
  body {
    font-family: "Roboto", Arial, sans-serif;
    color: var(--text);
    background: #fff;
    border-top: 3px solid var(--slate-dark);
  }
  .wrap { width: 860px; margin: 0 auto; position: relative; }

  .site-header { height: 107px; }
  .site-header .wrap { height: 100%; display: flex; align-items: center; justify-content: space-between; }
  .brand {
    font-size: 44px; font-weight: 700; color: var(--green);
    letter-spacing: -1px; margin-top: -8px;
  }
  .header-mail { display: flex; align-items: center; gap: 10px; font-size: 13px; margin-top: -16px; }
  .header-mail a { color: var(--text); }

  .main-nav {
    height: 33px;
    border-top: 1px solid #dcdcdc;
    background: linear-gradient(#fff, #e9e9e9);
  }
  .main-nav ul { list-style: none; display: flex; height: 33px; }
  .main-nav li {
    height: 33px; line-height: 33px; font-size: 13px; text-align: center;
    border-right: 1px solid #d2d2d2;
  }
  .main-nav li.active { background: var(--green); color: #fff; border-right: none; }

  .hero {
    height: 395px;
    background: linear-gradient(90deg, var(--sky-dark), var(--sky-light) 50%, var(--sky-dark));
  }
  .hero-slide {
    height: 395px; position: relative;
    background: radial-gradient(ellipse at 45% 45%, #b6b2a6 0%, #7a5f45 35%, #4a3627 75%, #3a2a1e 100%);
  }
  .hero-arrow {
    position: absolute; top: 173px; width: 50px; height: 50px; border-radius: 50%;
    background: rgba(235,235,235,0.85); display: flex; align-items: center; justify-content: center;
  }
  .hero-arrow.prev { left: 15px; }
  .hero-arrow.next { right: 15px; }
  .hero-caption {
    position: absolute; right: 0; top: 306px; width: 222px; height: 37px;
    background: var(--green); color: #fff; font-size: 23px; font-weight: 300;
    line-height: 37px; padding-left: 21px;
  }

  .welcome {
    height: 84px;
    background: linear-gradient(#ececec, #fff);
    text-align: center;
  }
  .welcome h1 { font-size: 23px; font-weight: 300; line-height: 104px; color: var(--text); }
  .welcome h1 span { color: var(--green); }
  .divider { border-top: 1px solid var(--rule); }

  .sectors { display: flex; justify-content: center; gap: 72px; padding-top: 26px; height: 321px; }
  .sector { width: 325px; text-align: center; }
  .sector h2 { font-size: 23px; font-weight: 300; margin-bottom: 17px; }
  .sector-frame {
    position: relative; height: 198px; padding: 4px; background: #fff;
    border: 1px solid #ddd;
    box-shadow: 0 12px 10px -8px rgba(0,0,0,0.45);
  }
  .sector-photo { width: 100%; height: 100%; }
  .sector-photo.forest { background: linear-gradient(#3e5a22, #7ca32e 55%, #a8c945); }
  .sector-photo.farm { background: linear-gradient(#b8cbe4, #a9a792 45%, #6f7a3e 80%, #8a9a3a); }
  .sector-btn {
    position: absolute; left: 50%; bottom: 4px; transform: translateX(-50%);
    background: var(--green); color: #fff; font-size: 13px;
    width: 114px; height: 35px; line-height: 35px;
  }

  .site-footer { background: var(--slate); height: 124px; text-align: center; color: #e6ebf0; }
  .site-footer h3 {
    font-size: 23px; font-weight: 300; padding-top: 13px;
    width: 332px; margin: 0 auto; padding-bottom: 6px;
    border-bottom: 1px solid #26333f;
  }
  .site-footer address { font-style: normal; font-size: 12px; line-height: 14px; margin-top: 12px; }
  .site-footer .footer-mail { color: var(--muted); font-size: 12px; margin-top: 9px; }
  .copyright {
    background: var(--slate-dark); height: 33px; line-height: 33px;
    text-align: center; color: #fff; font-size: 12px;
  }
</style>
</head>
<body>
  <header class="site-header">
    <div class="wrap">
      <div class="brand">SILVANE</div>
      <div class="header-mail">
        <svg width="22" height="18" viewBox="0 0 22 18" aria-hidden="true">
          <rect x="1" y="4" width="20" height="13" fill="#4f5e6d"/>
          <path d="M1 4 L11 11 L21 4" fill="none" stroke="#fff" stroke-width="1.5"/>
          <path d="M5 4 L11 0 L17 4" fill="#4f5e6d"/>
        </svg>
        <a href="#">info@silvane.com</a>
      </div>
    </div>
  </header>

  <nav class="main-nav">
    <ul class="wrap">
      <li class="active" style="width:87px">Home</li>
      <li style="width:112px">Emberless2</li>
      <li style="width:116px">Smart Agri</li>
      <li style="width:119px">Technology</li>
      <li style="width:109px">About us</li>
      <li style="width:111px">Contact us</li>
    </ul>
  </nav>

  <section class="hero">
    <div class="wrap hero-slide" role="img" aria-label="Photo of a white sensor box mounted on a wooden post among dry autumn leaves">
      <div class="hero-arrow prev">
        <svg width="14" height="26" viewBox="0 0 14 26"><path d="M12 1 L2 13 L12 25" fill="none" stroke="#777" stroke-width="1.5"/></svg>
      </div>
      <div class="hero-arrow next">
        <svg width="14" height="26" viewBox="0 0 14 26"><path d="M2 1 L12 13 L2 25" fill="none" stroke="#777" stroke-width="1.5"/></svg>
      </div>
      <div class="hero-caption">Internet of Things</div>
    </div>
  </section>

  <section class="welcome">
    <h1>Welcome to <span>Silvane SA</span> Website</h1>
  </section>
  <div class="wrap divider"></div>

  <section class="sectors">
    <article class="sector">
      <h2>Forest Fires</h2>
      <div class="sector-frame">
        <div class="sector-photo forest" role="img" aria-label="Photo of a solar-powered sensor station on a grassy forest slope"></div>
        <div class="sector-btn">VIEW DETAILS</div>
      </div>
    </article>
    <article class="sector">
      <h2>Agriculture</h2>
      <div class="sector-frame">
        <div class="sector-photo farm" role="img" aria-label="Photo of a sensor mounted on a pole in a hillside vineyard with a blossoming tree"></div>
        <div class="sector-btn">VIEW DETAILS</div>
      </div>
    </article>
  </section>

  <footer>
    <div class="site-footer">
      <h3>Reach Us</h3>
      <address>Silvane SA - Via dei Tigli 4 -<br>CH6900 Lugano Nord (Parco Tecno), Switzerland</address>
      <div class="footer-mail">Email - info@silvane.com</div>
    </div>
    <div class="copyright">Copyright © <strong>Silvane SA</strong> 2013. All rights reserved.</div>
  </footer>
</body>
</html>
```